依頼詳細
清潔感のあるイメージを希望しています。
できれば安心感を与える為、女性の写真などをいれてください。
掲載してもらいたい内容を載せています
宜しくお願いします。
①24時間営業
②6/6(金)新規オープン
③アクセスマップ(わかりにくい場所にあるので大きめに作成してください)
④6/30まで全機種半額
洗濯乾燥8kg 800円→400円
洗濯乾燥15kg 1000円→500円
洗濯のみ12kg 400円→200円
洗濯のみ22kg 600円→300円
乾燥のみ14kg 100円/11分→100円/22分
乾燥のみ25kg 100円/9分→100円/18分
⑤洗濯機から乾燥機に移す面倒な手間いらずの全自動洗濯乾燥機を導入
⑥となりのふとんクリーニング工場プロデュースなので
羽毛布団、こたつ布団、毛布の洗濯も安心
スタッフが工場に常駐なので安心
記載項目
社名(さらり堂コインランドリー)、住所(大分市椿原427-5)、地図(添付ファイル、キャラクターぴかりん、店舗写真、店内写真
サイズ
A4
ページ数
両面
希望イメージ
シンプル 複雑
単色 カラフル
暗い 明るい
日常 高級
遊び心 厳粛
未来的 伝統的
女性的 男性的
希望する色
納品ファイル
• 高解像度JPG (.jpg)
• イラストレーター形式 (.ai)
• フォトショップ形式 (.psd)
補足説明
店舗写真は添付の工場写真を当て込んでください。店内写真もまだ用意できていませんので空欄でお願いします。正式な写真は後日差し替えをお願いします。
添付の地図に近郊のお客様の目印になりそうな店名を追記しています。参考にしてください。場所が奥まっていますので地図は大きめに詳しく表記をお願いします。
納品はアウトライン化したものとしていないものの両方お願いします。
写真等のデータファイルを追加します
宜しくお願いします

```html
<!DOCTYPE html>
<html lang="ja">
<head>
<meta charset="utf-8">
<title>さらり堂コインランドリー オープニングキャンペーン</title>
<link href="https://fonts.googleapis.com/css2?family=M+PLUS+Rounded+1c:wght@500;800;900&family=Noto+Sans+JP:wght@400;700;900&display=swap" rel="stylesheet">
<style>
:root{
  --blue:#1f6fc4;
  --blue-dark:#0f4f9a;
  --sky:#e7f3fc;
  --green:#2fae4a;
  --orange:#f08a12;
  --red:#e63a2a;
  --ink:#333a44;
  --white:#ffffff;
  --gray:#b9c4cf;
}
*{margin:0;padding:0;box-sizing:border-box}
html,body{width:853px;height:1200px;overflow:hidden;background:var(--white)}
body{font-family:"Noto Sans JP",sans-serif;color:var(--ink)}
.flyer{position:relative;width:853px;height:1200px;overflow:hidden;
  background:linear-gradient(180deg,var(--sky) 0%,var(--white) 45%,var(--white) 100%)}

.store-photo{position:absolute;left:0;top:0;width:480px;height:240px;
  background:linear-gradient(135deg,#8fa7be 0%,#c9d6e2 45%,#6f8ba6 100%)}

.campaign{position:absolute;right:0;top:0;width:430px;height:490px;background:var(--white);
  border-bottom-left-radius:180px 120px;padding:26px 20px 0 36px}
.campaign-title{font-family:"M PLUS Rounded 1c",sans-serif;font-weight:900;color:var(--orange);
  font-size:22px;letter-spacing:0;text-align:center;white-space:nowrap}
.campaign-lead{font-size:12px;color:var(--ink);text-align:center;margin-top:6px}
.half-price{margin:8px auto 0;width:300px;border:3px solid var(--blue);border-radius:10px;
  text-align:center;font-family:"M PLUS Rounded 1c",sans-serif;font-weight:900;font-size:50px;
  color:var(--blue);line-height:1.2;background:#fffbe6}
.half-price em{font-style:normal;color:var(--red)}
.campaign-date{text-align:center;font-weight:700;color:var(--blue);font-size:15px;margin-top:6px}

.price-table{margin:12px 0 0 6px;border-collapse:collapse;font-weight:700;font-size:17px}
.price-table td{padding:3px 8px;border-bottom:1px dashed var(--gray);white-space:nowrap}
.price-table .label{color:var(--white);font-size:15px;line-height:1.15;text-align:center;width:64px;border-bottom:3px solid var(--white)}
.label.wash-dry{background:var(--blue)}
.label.wash{background:var(--green)}
.label.dry{background:var(--orange)}
.price-table .kg{text-align:right;color:var(--ink)}
.price-table .new{color:var(--red);font-size:19px}

.feature{position:absolute}
.feature h2{font-family:"M PLUS Rounded 1c",sans-serif;font-weight:900;line-height:1.2}
.feature p{font-size:14px;line-height:1.6;font-weight:700}
.auto{left:34px;top:290px;width:360px}
.auto h2{color:var(--green);font-size:32px}
.auto p{margin-top:8px;color:var(--ink)}
.shirt-art{position:absolute;left:260px;top:160px;width:140px;height:115px;border-radius:20px;
  background:linear-gradient(160deg,#d8ecfb,#9fcbef)}

.futon{left:34px;top:480px;width:330px}
.futon h2{color:var(--blue);font-size:32px}
.futon p{margin-top:10px}
.futon-art{position:absolute;left:310px;top:440px;width:110px;height:110px;border-radius:18px;
  background:linear-gradient(160deg,#fde3c6,#f4a45a)}
.bubble{position:absolute;left:290px;top:380px;width:130px;padding:8px;border:2px solid var(--orange);
  border-radius:50%;background:var(--white);font-size:10px;line-height:1.4;text-align:center;color:var(--orange);font-weight:700}

.open24{left:470px;top:500px;width:350px}
.open24 h2{color:var(--blue);font-size:40px}
.open24 p{margin-top:10px}
.clock{position:absolute;left:730px;top:470px}

.map{position:absolute;left:40px;top:700px;width:650px;height:410px;border:3px solid var(--blue);
  border-radius:8px;background:linear-gradient(135deg,#eef3e6,#dde9d3)}
.mascot{position:absolute;left:700px;top:980px;width:140px;height:150px;border-radius:50% 50% 20px 20px;
  background:linear-gradient(180deg,#f2a09a,#d8433a)}
.mascot-bubble{position:absolute;left:710px;top:900px;width:120px;height:70px;border:2px solid var(--blue);
  border-radius:50%;background:var(--white);display:flex;align-items:center;justify-content:center;
  text-align:center;font-size:13px;font-weight:700;color:var(--blue);line-height:1.3}

.footer{position:absolute;left:0;bottom:0;width:853px;height:62px;background:var(--blue);
  display:flex;align-items:center;justify-content:space-between;padding:0 34px;color:var(--white)}
.store-name{font-family:"M PLUS Rounded 1c",sans-serif;font-weight:800;font-size:26px}
.address{font-weight:700;font-size:17px}
</style>
</head>
<body>
<main class="flyer">
  <div class="store-photo" role="img" aria-label="店内に並ぶ洗濯乾燥機の写真"></div>

  <section class="campaign">
    <p class="campaign-title">オープニングキャンペーン実施中!!</p>
    <p class="campaign-lead">毎回のジメジメの時短で“うれしい”</p>
    <p class="half-price">全機種<em>半額</em>!</p>
    <p class="campaign-date">6月6日〜6月30日まで</p>
    <table class="price-table">
      <tr><td class="label wash-dry" rowspan="2">洗濯<br>乾燥</td><td class="kg">8kg</td><td>800円→<span class="new">400円</span></td></tr>
      <tr><td class="kg">15kg</td><td>1000円→<span class="new">500円</span></td></tr>
      <tr><td class="label wash" rowspan="2">洗濯<br>のみ</td><td class="kg">12kg</td><td>400円→<span class="new">200円</span></td></tr>
      <tr><td class="kg">22kg</td><td>600円→<span class="new">300円</span></td></tr>
      <tr><td class="label dry" rowspan="2">乾燥<br>のみ</td><td class="kg">14kg</td><td>100円/11分→<span class="new">100円/22分</span></td></tr>
      <tr><td class="kg">25kg</td><td>100円/9分→<span class="new">100円/18分</span></td></tr>
    </table>
  </section>

  <div class="shirt-art" role="img" aria-label="洗いたてのシャツのイラスト"></div>
  <section class="feature auto">
    <h2>全自動<br>洗濯乾燥機を導入!</h2>
    <p>洗濯機から乾燥機に移す<br>面倒な手間いらず</p>
  </section>

  <div class="bubble">気軽に安心して布団が洗えるようになったよ</div>
  <div class="futon-art" role="img" aria-label="ふとんにくるまる子どものイラスト"></div>
  <section class="feature futon">
    <h2>布団も<br>安心して洗える!</h2>
    <p>となりのふとんクリーニング工場プロデュースなので羽毛布団、こたつ布団、毛布の洗濯も安心して出来ます。<br>さらに、スタッフが工場に常駐なので安心です。</p>
  </section>

  <svg class="clock" width="70" height="70" viewBox="0 0 70 70" aria-hidden="true">
    <circle cx="35" cy="35" r="30" fill="#ffffff" stroke="#2fae4a" stroke-width="5"/>
    <line x1="35" y1="35" x2="35" y2="16" stroke="#333a44" stroke-width="4" stroke-linecap="round"/>
    <line x1="35" y1="35" x2="50" y2="40" stroke="#333a44" stroke-width="4" stroke-linecap="round"/>
  </svg>
  <section class="feature open24">
    <h2>24時間営業!</h2>
    <p>深夜や早朝でも、あなたのライフスタイルに<br>合わせてご利用できます</p>
  </section>

  <div class="map" role="img" aria-label="店舗周辺のアクセスマップ(大通り・病院・近隣店舗の目印付き)"></div>

  <div class="mascot-bubble">ご利用して<br>ください</div>
  <div class="mascot" role="img" aria-label="お店のマスコットキャラクターのイラスト"></div>

  <footer class="footer">
    <span class="store-name">さらり堂コインランドリー</span>
    <span class="address">大分市椿原427-5</span>
  </footer>
</main>
</body>
</html>
```